insert for clam shell / vape cartridge

Brand : Brevor (roman god of fire)
card insert dimensions are 2.5" in width and 3.375" in height
this is a cannabis product. Open to any and all designs. Currently using very generic text. 5/8" on left edge of design will be covered by the cartridge

Target Market(s)

medical cannabis patients

Industry/Entity Type

Product

Logo Text

Brevor

Requirements
Must have
• logo
Nice to have
• "distilled cannabis oil"
• "no pg/vg"
• subtle use of cannabis leaf
Should not have
• no big (prominent) Pot leaves

```html
<!DOCTYPE html>
<html lang="en">
<head>
<meta charset="utf-8">
<title>Brevor – Cartridge Insert</title>
<link href="https://fonts.googleapis.com/css2?family=Marcellus+SC&display=swap" rel="stylesheet">
<style>
  :root {
    --page-bg: #ffffff;
    --teal-deep: #112c36;
    --teal-mid: #1a3f4b;
    --teal-stripe: #24566a;
    --lime: #a8d13b;
    --lime-dark: #86b83a;
    --ink-light: #ffffff;
    --ink-dark: #163540;
    --mark-grey: #c9cacb;
  }
  * { margin: 0; padding: 0; box-sizing: border-box; }
  html, body {
    width: 1200px; height: 906px; overflow: hidden;
    background: var(--page-bg);
    font-family: "Marcellus SC", "Copperplate", serif;
  }
  .canvas { position: relative; width: 1200px; height: 906px; }

  .insert-card {
    position: absolute; left: 118px; top: 118px;
    width: 499px; height: 674px; overflow: hidden;
  }
  .insert-card__art { position: absolute; inset: 0; }

  .brand-mark {
    position: absolute; border-radius: 50%;
  }
  .insert-card .brand-mark {
    left: 263px; top: 69px; width: 120px; height: 120px;
    background: var(--ink-light);
  }

  .brand-name {
    position: absolute; white-space: nowrap; text-align: center; line-height: 1;
  }
  .insert-card .brand-name {
    left: 173px; top: 197px; width: 300px;
    font-size: 50px; letter-spacing: 3px; color: var(--ink-light);
  }

  .product-type {
    position: absolute; left: 210px; top: 300px;
    color: var(--ink-light); font-size: 22px; letter-spacing: 3px; line-height: 24px;
  }
  .product-type__oil {
    display: flex; align-items: center; gap: 7px;
    font-size: 29px; line-height: 32px; margin-top: 1px;
  }
  .leaf-icon { width: 17px; height: 17px; border-radius: 50%; background: var(--lime); display: inline-block; }

  .claim-band {
    position: absolute; left: 210px; top: 440px; width: 196px; height: 31px;
    background: linear-gradient(90deg, var(--lime) 0%, var(--lime) 72%, rgba(168,209,59,0) 100%);
    color: var(--ink-dark); font-size: 21px; letter-spacing: 2px;
    padding-left: 11px; line-height: 32px;
  }
  .leaf-note {
    position: absolute; left: 211px; top: 484px;
    color: var(--ink-light); font-size: 22px; letter-spacing: 3px; line-height: 24px;
  }
  .net-weight {
    position: absolute; left: 346px; top: 621px;
    color: var(--ink-light); font-size: 20px; letter-spacing: 3px; line-height: 24px;
  }

  .brand-lockup { position: absolute; inset: 0; pointer-events: none; }
  .brand-lockup .brand-mark {
    left: 850px; top: 288px; width: 200px; height: 200px;
    background: var(--mark-grey);
  }
  .brand-lockup .brand-name {
    left: 734px; top: 505px; width: 420px;
    font-size: 74px; letter-spacing: 5px; color: var(--mark-grey);
  }
</style>
</head>
<body>
<main class="canvas">

  <section class="insert-card" aria-label="Cartridge card insert">
    <svg class="insert-card__art" width="499" height="674" viewBox="0 0 499 674" aria-hidden="true">
      <defs>
        <linearGradient id="teal-field" x1="0" y1="0" x2="0" y2="1">
          <stop offset="0" stop-color="var(--teal-deep)"/>
          <stop offset="1" stop-color="var(--teal-mid)"/>
        </linearGradient>
        <linearGradient id="lime-top" x1="0" y1="0" x2="0" y2="1">
          <stop offset="0" stop-color="#b4d84a"/>
          <stop offset="0.5" stop-color="var(--lime)"/>
          <stop offset="0.52" stop-color="var(--lime-dark)"/>
          <stop offset="1" stop-color="#8fbf3c"/>
        </linearGradient>
        <linearGradient id="lime-bottom" x1="0" y1="0" x2="1" y2="1">
          <stop offset="0" stop-color="var(--lime-dark)"/>
          <stop offset="1" stop-color="#b8dc4c"/>
        </linearGradient>
        <clipPath id="stripe-zone">
          <polygon points="210,420 499,300 499,674 300,674"/>
        </clipPath>
      </defs>

      <rect width="499" height="674" fill="url(#teal-field)"/>

      <g class="stripes" clip-path="url(#stripe-zone)" stroke="var(--teal-stripe)" stroke-width="5" opacity="0.6">
        <line x1="100" y1="400" x2="400" y2="700"/>
        <line x1="120" y1="400" x2="420" y2="700"/>
        <line x1="140" y1="400" x2="440" y2="700"/>
        <line x1="160" y1="400" x2="460" y2="700"/>
        <line x1="180" y1="400" x2="480" y2="700"/>
        <line x1="200" y1="400" x2="500" y2="700"/>
        <line x1="220" y1="400" x2="520" y2="700"/>
        <line x1="240" y1="400" x2="540" y2="700"/>
        <line x1="260" y1="400" x2="560" y2="700"/>
        <line x1="280" y1="400" x2="580" y2="700"/>
        <line x1="300" y1="400" x2="600" y2="700"/>
        <line x1="320" y1="400" x2="620" y2="700"/>
        <line x1="340" y1="400" x2="640" y2="700"/>
      </g>

      <polygon class="lime-corner-top" points="0,0 236,0 0,227" fill="url(#lime-top)"/>
      <polygon class="lime-corner-bottom" points="0,478 102,574 258,574 350,674 0,674" fill="url(#lime-bottom)"/>
      <polygon points="102,574 258,574 350,674 200,674" fill="#b8db4e" opacity="0.55"/>

      <g class="chevrons" fill="none" stroke="var(--lime)" stroke-width="7">
        <polyline points="499,216 372,342 499,468"/>
        <polyline points="499,250 406,342 499,434"/>
        <polyline points="499,282 440,342 499,402"/>
        <polyline points="499,312 470,342 499,372"/>
      </g>

      <line class="fold-line" x1="125" y1="0" x2="125" y2="674" stroke="#ffffff" stroke-width="1.5" stroke-dasharray="9 7"/>
    </svg>

    <span class="brand-mark" aria-hidden="true"></span>
    <div class="brand-name">BREVOR</div>

    <div class="product-type">
      <div>DISTILLED</div>
      <div>CANNABIS</div>
      <div class="product-type__oil"><span class="leaf-icon" role="img" aria-label="Small cannabis leaf icon"></span>OIL</div>
    </div>

    <div class="claim-band">NO PG/VG</div>

    <div class="leaf-note">
      <div>SUBTLE USE OF</div>
      <div>CANNABIS LEAF</div>
    </div>

    <div class="net-weight">1 GRAM</div>
  </section>

  <section class="brand-lockup" aria-label="Brand name">
    <span class="brand-mark" aria-hidden="true"></span>
    <div class="brand-name">BREVOR</div>
  </section>

</main>
</body>
</html>
```